Exclusive beauty salon needs a price list or services booklet

I need a new very attractive flyer for my beauty salon, containing information on the different services and their prices.
In attachment you can find a pdf of the "old" one, but I'd love to have a beautifully designed new one!
I'd love to have a booklet in format 148 x 148 mm, or in US format, containing 12 or 16 pages, but if you can offer other nice looking designs they are welcome!
The services that need to come in the booklet with their prices can all be found on my website: www.atelierkova.be, starting with
Gelaatsverzorging
Wimperverlenging
Suikerontharing
Wimperlifting
Permanente Make Up
Airbrush Tanning

Target Market(s)

woman from 20 to 89 years old

Industry/Entity Type

Beauty Salon

Font styles to use
Sans Serif

Colors

Designer to choose colors to be used in the design.

Requirements
Must have
• a classy nice look, it must contain details about the services from my beauty salon and their prices, and nice pictures.
• The Names, prices and explanations of the services can easily be found on my website: www.atelierkova.be
Nice to have
• In attachment you can find the "old" price list in pdf, what I need now is a "new booklet" with the new logo and updated services price list.
• I need a very nice and attractive looking booklet, classy chique, Paris chique, looking very expensive.
Should not have
• Not too much colors, not too curly, but still feminine

```html
<!DOCTYPE html>
<html lang="nl">
<head>
<meta charset="utf-8">
<title>Wimperlifting &amp; Permanente Make Up – booklet spreads</title>
<link href="https://fonts.googleapis.com/css2?family=Raleway:wght@400;500;600;700;800&display=swap" rel="stylesheet">
<style>
  :root {
    --backdrop: #e9e4e2;
    --ink: #2b2a2c;
    --tab: #353234;
    --rose: #e9a9b7;
    --rose-soft: #f6d8e0;
    --rose-page: #f5d6de;
    --rose-deep: #e6b2bb;
    --rose-light: #f3d2d7;
    --stripe: #f4c7d1;
    --white: #ffffff;
    --lip: #c2185b;
  }
  * { box-sizing: border-box; margin: 0; padding: 0; }
  html, body { width: 1200px; height: 1000px; overflow: hidden; }
  body {
    background: var(--backdrop);
    font-family: "Raleway", Arial, sans-serif;
    color: var(--ink);
    position: relative;
  }
  .page { position: absolute; overflow: hidden; }
  .spread-top .page { top: 18px; height: 467px; }
  .spread-bottom .page { top: 507px; height: 466px; }
  .page-left { left: 133px; width: 467px; }
  .page-right { left: 600px; width: 467px; }

  .stripes { position: absolute; height: 18px; }
  .stripes::before, .stripes::after {
    content: ""; position: absolute; left: 0; right: 0; background: var(--stripe);
  }
  .stripes::before { top: 0; height: 8px; }
  .stripes::after { top: 11px; height: 5px; }

  .title-tab {
    position: absolute; top: 0; background: var(--tab);
    border-radius: 0 0 14px 14px;
    display: flex; flex-direction: column; justify-content: center; align-items: center;
    color: var(--rose);
  }
  .page-number {
    position: absolute; bottom: 2px; width: 27px; height: 25px;
    background: var(--tab); color: var(--white);
    font-size: 9px; font-weight: 700;
    display: flex; align-items: center; justify-content: center;
  }

  .copy { position: absolute; font-size: 9.2px; line-height: 11.1px; }
  .copy p { margin-bottom: 11px; }
  .copy h3 { font-size: 9.4px; font-weight: 700; }
  .copy ul { list-style: none; }
  .copy li::before { content: "● "; font-size: 7px; vertical-align: 1px; }

  /* page 07 */
  .p07 { background: var(--white); }
  .p07 .stripes { left: 175px; right: 0; top: 10px; }
  .p07 .title-tab { left: 14px; width: 161px; height: 160px; }
  .p07 .title-tab span { font-size: 24px; font-weight: 800; letter-spacing: 1px; line-height: 32px; }
  .brand {
    position: absolute; left: 30px; top: 190px; width: 110px;
    display: flex; align-items: center; gap: 6px;
    font-size: 14px; font-weight: 700; color: var(--ink);
  }
  .brand i { width: 10px; height: 10px; background: var(--ink); display: block; }
  .photo { position: absolute; }
  .photo-label {
    position: absolute; right: 6px; bottom: 6px;
    font-size: 8px; font-weight: 700; color: var(--ink);
  }
  .p07 .photo { left: 42px; width: 105px; height: 87px; }
  .p07 .photo.before { top: 260px; background: linear-gradient(160deg, #b89a84, #d8c1ae 55%, #a98c78); }
  .p07 .photo.after { top: 357px; background: linear-gradient(160deg, #c9b3a3, #e2d3c8 50%, #8f7f74); }
  .p07 .copy { left: 185px; top: 38px; width: 275px; }
  .p07 .copy .lead { font-size: 12px; font-weight: 700; line-height: 13px; }
  .p07 .cols { display: flex; gap: 6px; }
  .p07 .page-number { right: 2px; }

  /* page 08 */
  .p08 { background: linear-gradient(180deg, var(--rose-deep), var(--rose-light)); }
  .p08 .stripes { left: 0; right: 0; top: 10px; }
  .p08 .copy { left: 13px; top: 40px; width: 445px; }
  .p08 .page-number { right: 0; }

  /* page 09 */
  .p09 { background: var(--rose-page); }
  .p09 .stripes { left: 0; right: 0; top: 5px; }
  .p09 .copy { left: 13px; top: 72px; width: 445px; font-size: 8.9px; line-height: 10.9px; }
  .p09 h2 { font-size: 12px; font-weight: 800; margin-bottom: 1px; }
  .p09 section { margin-bottom: 28px; }
  .p09 .page-number { left: 440px; }

  /* page 10 */
  .p10 { background: var(--rose-page); }
  .p10 .title-tab { left: 17px; width: 161px; height: 160px; color: var(--white); }
  .p10 .title-tab .line1 { font-size: 18px; font-weight: 400; letter-spacing: 1px; }
  .p10 .title-tab .line2 { font-size: 22px; font-weight: 700; letter-spacing: 3px; color: var(--rose); }
  .p10 .hero {
    position: absolute; left: 178px; top: 0; width: 289px; height: 466px;
    background: linear-gradient(170deg, #e9e0dc 0%, #d47a98 38%, #b0234f 62%, #e4b6a8 100%);
  }
  .p10 .detail {
    position: absolute; left: 32px; top: 176px; width: 134px; height: 82px;
    background: var(--white); padding: 4px;
  }
  .p10 .detail div { width: 100%; height: 100%; background: linear-gradient(150deg, #9a6f64, #7a2f3a 50%, #c49a8d); }
  .p10 .copy { left: 32px; top: 268px; width: 146px; font-size: 8.6px; line-height: 10.2px; }
  .price-line { font-size: 12px; font-weight: 800; }
  .price-line .dots { font-size: 8px; font-weight: 400; }
  .p10 li { padding-left: 9px; text-indent: -9px; }
  .p10 .page-number { right: 0; }
</style>
</head>
<body>

<div class="spread-top">
  <div class="page page-left p07">
    <div class="stripes"></div>
    <div class="title-tab"><span>WIMPER-</span><span>LIFTING</span></div>
    <div class="brand"><i></i>Luma Lashes</div>
    <div class="photo before" role="img" aria-label="Close-up of an eye before the lash lift"><span class="photo-label">BEFORE</span></div>
    <div class="photo after" role="img" aria-label="Close-up of an eye with lifted lashes after treatment"><span class="photo-label">AFTER</span></div>
    <div class="copy">
      <p><span class="lead">Luma = Lenght • Volume • Lift</span><br>voor uw natuurlijke wimpers.</p>
      <p>Het hebben van mooie, lange en volumineuze wimpers staat hoog op het verlanglijstje van vele vrouwen. Het liefst heeft men de wimpers mooi gelift voor een open blik die de ogen optisch groter maakt. Niet voor niets is mascara één van de best verkochte make-upproducten.</p>
      <p>De nieuwe en revolutionaire Luma-methode zorgt echter na slechts 1 behandeling van 60 minuten, gedurende minimaal 6 weken voor Lange, Volumineuze en geLifte wimpers. Dit alles, zonder dat daar een wimperkrultang of dikke lagen mascara aan te pas hoeven te komen!</p>
      <h3>Hoe werrktt hett??</h3>
      <p>De revolutionaire Luma- methode is een behandeling voor de eigen wimpers, waarbij géén gebruik wordt gemaakt van het aanbrengen van valse wimpers. Bij deze bijzondere behandeling die volledig nieuw is, wordt een laagje 'coating' aangebracht bij de wimperaanzet met een nieuw soort gelformule. Dan bepalen we aan de hand van uw wimperlengte de curve van het siliconen schildje. Door middel van dit siliconen schildje worden de wimpers effectief gelift vanaf de wimperaanzet (dus vanaf de wortel), hetgeen zorgt voor een open blik met lange, volumineuze en perfect gesepareerde wimpers.</p>
      <p>Door ook nog een tint nadien toe te voegen, krijgen de wimpers meteen een super color boost!</p>
      <p>De sessie heeft 24u nodig om te fixeren. Het is dus ook niet aan te raden de behandeling te kort voor het slapen te ondergaan.</p>
      <div>De eerste 24u:</div>
      <div class="cols">
        <ul><li>Geen water aan de ogen</li><li>Geen make-up aan de ogen</li><li>Geen oogcrème</li></ul>
        <ul><li>Niet wrijven in de ogen</li><li>Geen sauna, zwem -of stoombad</li></ul>
      </div>
    </div>
    <div class="page-number">07</div>
  </div>

  <div class="page page-right p08">
    <div class="stripes"></div>
    <div class="copy">
      <p>Wimperlifting is een techniek die wimperverbetering en verven combineert, een unieke combinatie!</p>
      <div>Wimperlifting blijft 4 tot 6 weken zitten.</div>
      <ul style="margin-bottom:11px">
        <li>Je hebt geen mascara of wimperkrultang meer nodig.</li>
        <li>Voelt licht en natuurlijk aan.</li>
        <li>Uw ogen lijken groter.</li>
        <li>De Wimperlift is niet schadelijk voor de eigen wimpers.</li>
        <li>Bestand tegen water, douchen, zweten, tranen, zwemmen en slapen.</li>
      </ul>
      <h3>Wat is het verschil tussen Wimperlifting en Wimperpermanent?</h3>
      <p>Bij het zetten van wimperpermanent worden er klemmen en/of rollers gebruikt. Door deze methode kan er slechts een gedeelte van de wimpers behandeld worden, waardoor u broze wimpers kunt krijgen en wimperhaartjes afbreken. De Wimperlift daarentegen is totaal niet schadelijk voor uw wimpers!</p>
      <div>U kunt GEEN wimperlift behandeling ondergaan wanneer u:</div>
      <ul style="margin-bottom:11px">
        <li>een infectie heeft van de Zeis klieren (bekend als "een strontje").</li>
        <li>uw wimpers zijn uitgevallen als gevolg van Alopecia of chemotherapie.</li>
        <li>lijdt aan conjunctivitis.</li>
        <li>lijdt aan trichotillomanie.</li>
        <li>zwanger bent of borstvoeding geeft.</li>
        <li>in het verleden last heeft gehad van haaruitval.</li>
        <li>extreem korte of extreem fijne wimpers heeft.</li>
      </ul>
      <div>Wanneer u last heeft van onderstaande aandoeningen is het WEL MOGELIJK om een wimperlift behandeling te ondergaan er wordt dan voorafgaand aan de behandeling een allergietest afgenomen:</div>
      <ul style="margin-bottom:11px">
        <li>Droge ogen syndroom.</li>
        <li>Wanneer u veel last heeft van allergieën.</li>
      </ul>
      <div>De behandelling</div>
      <ul style="font-weight:700">
        <li>Voorbereiding:</li>
        <li>De behandeling zelf:</li>
        <li>Einde van de behandeling.</li>
        <li>Enkele feiten:</li>
        <li>Het effect: wimperlift</li>
      </ul>
    </div>
    <div class="page-number">08</div>
  </div>
</div>

<div class="spread-bottom">
  <div class="page page-left p09">
    <div class="stripes"></div>
    <div class="copy">
      <section>
        <h2>PERMANENTE MAKE UP</h2>
        <div>Permanente make-up zit altijd goed en zorgt ervoor dat je er altijd verzorgd uitziet. Eyeliners, lipliners of wenkbrauw- accenten worden permanent aangebracht. Zo zie je er tijdens het sporten, als je uit bed stapt, als je op vakantie uit zee komt, als je een fikse strandwandeling maakt of in de regen hebt gefietst, toch verzorgd uit. Permanente make-up blijft altijd op z'n plaats, daardoor oogt je gezicht ook na het verwijderen van je make-up niet 'kaal'. De aangebrachte accenten zorgen voor een sprekend gezicht en dat scheelt dagelijks een hoop tijd! Over permanente make-up moet je niet in een opwelling beslissen, je krijgt alle kans om er na het eerste consult nog eens goed over na te denken en ook als je er van af ziet, is dat geen enkel probleem. We zetten het alleen als je er 100% zeker van bent.</div>
      </section>
      <section>
        <h2>WAT IS PERMANENTE MAKE UP?</h2>
        <div>Permanente make up, micro-pigmentatie, cosmetische tatoeage, esthetische tatoeage of dermografie is een verfijnde tatoeage/ pigmentatietechniek van inplanting van hoge kwaliteitspigmenten op basis van mineralen onder de epidermis (=opperhuid). De behandeling wordt in uiterst hygiënische en veilige omstandigheden uitgevoerd met een professioneel apparaat en éénmalige, steriele naalden. Het doel van permanente make-up is het esthetische aspect verbeteren, waarbij het welzijn van de klant centraal staat. Het beoogde resultaat is natuurlijk en dit op langere termijn. Indien je op zoek bent naar een esthetische verbetering, een fysische correctie, een oplossing voor een specifiek fysisch probleem op je gelaat of lichaam kan permanente make up de juiste oplossing zijn.</div>
      </section>
      <section>
        <h2>WANNEER IS PERMANENTE MAKE- UP ZINVOL?</h2>
        <div>U wil er beter uitzien waardoor u zich beter voelt U wil een natuurlijke uitstraling, elke dag opnieuw U zoekt een waterbestendige make- up, geen make- up die uitloopt wanneer u geniet van wellness. Omwille van motorische of gezichtsproblemen is het moeilijk u correct te maquilleren U beheerst niet de tekenkunst om u juist te maquilleren<br>Beroepshalve bent u genoodzaakt er steeds gemaquilleerd, verzorgd uit te zien</div>
      </section>
    </div>
    <div class="page-number">09</div>
  </div>

  <div class="page page-right p10">
    <div class="hero" role="img" aria-label="Close-up of red lips and manicured hands holding a pink rose"></div>
    <div class="title-tab"><span class="line1">PERMANENTE</span><span class="line2">MAKE UP</span></div>
    <div class="detail" role="img" aria-label="Close-up of lips with permanent lip colour"><div></div></div>
    <div class="copy">
      <div class="price-line">FULL LIPS <span class="dots">...................</span>€595</div>
      <div>Een kleuraccent aan uw mond</div>
      <ul>
        <li>Uw hertekende liplijn preciseert uw natuurlijke mond</li>
        <li>Een schaduweffect waarbij de liplijn uitschaduwt op de mond</li>
        <li>Full lips vervolledigt de natuurlijke lipkleur</li>
        <li>Camoufleert oneffenheden zoals pigmentvlekjes, hypopigmentatie</li>
        <li>Vergroot boven en/ of onderlip</li>
        <li>Full lips kleurt de mond volledig</li>
      </ul>
    </div>
    <div class="page-number">10</div>
  </div>
</div>

</body>
</html>
```